VENTRIX Hardware needs a Flyer Designed

We need a flyer designed for a marketing strategy that is to be launched by VENTRIX. As it is for our hardware division, our logo should go unto the flyer. We are offering to our customers financing on items from $5000 up to $35000. Here are some key words that you may want to include; "building or revovating? you pick the job we've got the financing." The flyer should reflect some sort of home construction and should be very attractive and vibrant. On the flyer it should also state that it's "hassle-free" and; "no down payment", "no collateral", "affordable monthly payments".

Must Haves [en ]: The companies logo. Also it must state the address of the company and contact info which is; 47 Bellweather Lane Penal, Trinidad. Tel: 868-55-VENTRIX. Email must also be listed: info@ventrixholdings.example.

Nice To Haves [en ]: Good quality graphics. something that is captivating and that will hold the attention of our audience.

Should Not Haves [en ]: Should not be too busy.

Industry/Entity Type

Marketing

Requirements
Must have
• The companies logo. Also it must state the address of the company and contact info which is; 47 Bellweather Lane Penal, Trinidad. Tel: 868-55-VENTRIX. Email must also be listed: info@ventrixholdings.example.
Nice to have
• Good quality graphics. something that is captivating and that will hold the attention of our audience.
Should not have
• Should not be too busy.

```html
<!DOCTYPE html>
<html lang="en">
<head>
<meta charset="utf-8">
<title>VENTRIX Hardware – Building or Renovating Flyer</title>
<link href="https://fonts.googleapis.com/css2?family=Montserrat:ital,wght@1,900&family=Roboto:wght@400;500;700;900&display=swap" rel="stylesheet">
<style>
  :root {
    --navy: #1c2757;
    --red: #e0192f;
    --yellow: #ffe21a;
    --white: #ffffff;
    --stage: #eceef1;
    --photo-light: #d9cdbb;
    --photo-mid: #a88a66;
    --photo-dark: #6b5440;
  }
  * { margin: 0; padding: 0; box-sizing: border-box; }
  html, body { width: 1200px; height: 1130px; overflow: hidden; }
  body {
    background: var(--stage);
    font-family: "Roboto", Arial, sans-serif;
    position: relative;
  }
  .flyer {
    position: absolute;
    left: 230px; top: 42px;
    width: 740px; height: 1046px;
    background: var(--navy);
    overflow: hidden;
    box-shadow: 0 18px 40px rgba(0,0,0,0.25);
  }
  .hero-photo {
    position: absolute; left: 0; top: 0;
    width: 740px; height: 470px;
    background:
      radial-gradient(ellipse at 78% 55%, var(--photo-mid) 0%, rgba(168,138,102,0) 45%),
      linear-gradient(100deg, #f4f2ee 0%, #e8e2d8 35%, var(--photo-light) 60%, var(--photo-dark) 100%);
  }
  .headline-band {
    position: absolute; left: 0; top: 380px;
    width: 740px; height: 220px;
  }
  .headline {
    position: absolute; left: 0; top: 418px;
    width: 740px;
    text-align: center;
    font-family: "Montserrat", Arial, sans-serif;
    font-weight: 900; font-style: italic;
    line-height: 1;
    transform: rotate(-4deg);
  }
  .headline__line { display: block; letter-spacing: -1px; }
  .headline__line--navy { color: var(--navy); font-size: 60px; }
  .headline__line--white {
    color: var(--white); font-size: 68px; margin-top: 6px;
    text-shadow: 3px 3px 0 var(--navy), -2px -2px 0 var(--navy), 2px -2px 0 var(--navy), -2px 2px 0 var(--navy);
  }
  .tagline {
    position: absolute; left: 68px; top: 590px;
    color: var(--yellow);
    font-weight: 700; font-size: 41px; line-height: 1.2;
    text-transform: uppercase;
  }
  .divider {
    position: absolute; left: 68px; top: 704px;
    width: 560px; border-top: 2px dotted rgba(255,255,255,0.7);
  }
  .offer {
    position: absolute; left: 68px; top: 722px;
    color: var(--white); font-size: 25px;
  }
  .offer__amount { color: var(--yellow); font-weight: 700; }
  .benefits {
    position: absolute; left: 68px; top: 778px;
    list-style: none; color: var(--white); font-size: 23px;
  }
  .benefits li { display: flex; align-items: center; height: 37px; }
  .benefits svg { width: 20px; height: 20px; margin-right: 16px; }
  .contact-band {
    position: absolute; left: 0; top: 903px;
    width: 740px; height: 109px;
    background: var(--red);
  }
  .contact {
    position: absolute; left: 68px; top: 928px;
    width: 440px;
    color: var(--white); font-size: 18px; line-height: 1.75;
    font-style: normal; white-space: nowrap;
  }
  .contact__phone { color: var(--yellow); font-weight: 700; }
  .contact__sep { margin: 0 7px; }
  .brand-tile {
    position: absolute; left: 536px; top: 890px;
    width: 150px; height: 126px;
    background: var(--white);
    display: flex; align-items: center; justify-content: center;
    box-shadow: 0 4px 10px rgba(0,0,0,0.25);
  }
  .brand-tile__name {
    font-family: "Roboto", Arial, sans-serif;
    font-weight: 900; font-size: 28px;
    color: var(--navy); letter-spacing: 1px;
  }
</style>
</head>
<body>
  <article class="flyer">
    <div class="hero-photo" role="img" aria-label="Photo of a couple embracing in a newly renovated kitchen, half shown as a construction sketch"></div>

    <svg class="headline-band" viewBox="0 0 740 220" aria-hidden="true">
      <polygon points="0,75 740,23 740,100 0,152" fill="#ffffff"/>
      <polygon points="0,140 740,88 740,148 0,200" fill="#e0192f"/>
    </svg>

    <h1 class="headline">
      <span class="headline__line headline__line--navy">BUILDING OR</span>
      <span class="headline__line headline__line--white">RENOVATING?</span>
    </h1>

    <p class="tagline">You pick the job,<br>we’ve got the finances!</p>

    <div class="divider"></div>

    <p class="offer">Get up to <span class="offer__amount">$35,000.00</span> hassle-free at</p>

    <ul class="benefits">
      <li><svg viewBox="0 0 20 20"><path d="M3 10 L8 15 L17 4" fill="none" stroke="#ffffff" stroke-width="2"/></svg>No Down-payment</li>
      <li><svg viewBox="0 0 20 20"><path d="M3 10 L8 15 L17 4" fill="none" stroke="#ffffff" stroke-width="2"/></svg>No Collateral</li>
      <li><svg viewBox="0 0 20 20"><path d="M3 10 L8 15 L17 4" fill="none" stroke="#ffffff" stroke-width="2"/></svg>Affordable Monthly Payments</li>
    </ul>

    <div class="contact-band"></div>
    <address class="contact">
      47 Bellweather Lane Penal, Trinidad.<br>
      <span class="contact__phone">868-55-VENTRIX</span><span class="contact__sep">|</span>info@ventrixholdings.example
    </address>

    <div class="brand-tile">
      <span class="brand-tile__name">VENTRIX</span>
    </div>
  </article>
</body>
</html>
```